Poster Design Project- New Years Eve

We are a fun and quirky bar in St Kilda (www.quillhouse.com.au). We need a poster designed for our New Years Eve Event- details as follows
Project: A1 poster-NYE
Name of Event: Copper Moons
Date of Event: New Years Eve: 31.12.12
Tagline: ‘What happens at Quill stays at Quill’
Time: 8pm-3am
Cost:
$105 all inclusive
-Includes a cocktail on arrival
-4 hour drink package – Basic Spirits, Premium Beer, Wine and Sparkling til 12AM
-Grazing style canapés and finger food
Early bird and group discounts (10+) available
Purchase your tickets at the bar or through the website
Dress: For Fun and Dancing
Venue information:
• Address: 47 Brambleton Lane St Kilda
• Phone: 6143 2057
• Email: info@quillhouse.com.au
• Website: www.quillhouse.com.au
• Management reserves the right to refuse entry
Images: Images need to be high resolution or vector images so clarity is not lost when the poster is blown up to this size
Poster production:
Poster needs to be created in either Adobe Illustrator or Photoshop so we can easily edit the details if they change after the contest ends
Please provide 3mm internal and external bleed
Theming:
Fun poster with elements of Las Vegas including: dice/casino element, Las Copper Moons, pretty girls, cocktails
25-40 year olds
Casino

```html
<!DOCTYPE html>
<html lang="en">
<head>
<meta charset="utf-8">
<title>Copper Moons – New Years Eve at Quill</title>
<link rel="stylesheet" href="https://fonts.googleapis.com/css2?family=Anton&family=Bebas+Neue&family=Great+Vibes&display=swap">
<style>
  :root {
    --ink-night: #140b26;
    --deep-violet: #2a1446;
    --stage-purple: #6a2c9a;
    --stage-pink: #e04fb6;
    --stage-blue: #3b5fd0;
    --stage-gold: #f2c230;
    --title-yellow: #fff04a;
    --title-amber: #e8b51d;
    --accent-yellow: #f7e97a;
    --tag-cyan: #b9f3ff;
    --glow-cyan: #2fc8ff;
    --glow-pink: #ff4fd8;
    --paper-white: #ffffff;
    --muted-white: #d9d3ea;
  }
  * { box-sizing: border-box; margin: 0; padding: 0; }
  html, body { width: 853px; height: 1200px; overflow: hidden; background: var(--ink-night); }
  .poster {
    position: relative;
    width: 853px;
    height: 1200px;
    overflow: hidden;
    font-family: "Bebas Neue", "Arial Narrow", sans-serif;
    color: var(--paper-white);
  }
  .stage-scene {
    position: absolute;
    inset: 0;
    background:
      radial-gradient(ellipse 40% 30% at 22% 20%, rgba(224,79,182,0.75), transparent 70%),
      radial-gradient(ellipse 35% 30% at 78% 18%, rgba(242,194,48,0.55), transparent 70%),
      radial-gradient(ellipse 30% 25% at 60% 28%, rgba(59,95,208,0.55), transparent 70%),
      radial-gradient(ellipse 60% 40% at 50% 10%, rgba(106,44,154,0.9), transparent 80%),
      linear-gradient(180deg, var(--stage-purple) 0%, var(--deep-violet) 42%, var(--ink-night) 70%, #1c0f33 100%);
  }
  .crowd-band {
    position: absolute;
    left: 0; right: 0; top: 300px; height: 190px;
    background: linear-gradient(180deg, rgba(20,11,38,0) 0%, rgba(20,11,38,0.75) 55%, rgba(20,11,38,0) 100%);
  }
  .event-title {
    position: absolute;
    left: 0; right: 0; top: 262px;
    text-align: center;
  }
  .event-title__main {
    display: block;
    font-family: "Anton", "Impact", sans-serif;
    font-size: 196px;
    line-height: 1;
    letter-spacing: -2px;
    background: linear-gradient(180deg, var(--title-yellow) 0%, var(--title-yellow) 55%, var(--title-amber) 100%);
    -webkit-background-clip: text;
    background-clip: text;
    color: transparent;
  }
  .event-title__script {
    display: block;
    margin-top: -78px;
    margin-left: 70px;
    font-family: "Great Vibes", cursive;
    font-size: 140px;
    line-height: 1;
    color: var(--paper-white);
    text-shadow: 0 0 6px var(--glow-pink), 0 0 18px var(--glow-cyan), 0 0 30px var(--glow-pink);
  }
  .event-details {
    position: absolute;
    left: 0; right: 0; top: 606px;
    text-align: center;
  }
  .event-date { font-size: 40px; line-height: 1; letter-spacing: 1px; }
  .event-tagline {
    margin-top: 18px;
    font-size: 54px;
    line-height: 1;
    letter-spacing: 1.5px;
    color: var(--tag-cyan);
    text-shadow: 0 0 8px var(--glow-cyan), 0 0 20px var(--glow-cyan);
  }
  .event-time { margin-top: 20px; font-size: 44px; line-height: 1; letter-spacing: 1px; }
  .package {
    position: absolute;
    left: 60px; top: 814px;
  }
  .package__price { font-size: 27px; color: var(--accent-yellow); letter-spacing: 0.5px; }
  .package__list { list-style: none; margin-top: 6px; }
  .package__list li {
    position: relative;
    padding-left: 6px;
    font-size: 16px;
    line-height: 25px;
    letter-spacing: 0.5px;
  }
  .package__list li svg { position: absolute; left: -15px; top: 6px; }
  .ticket-notes {
    position: absolute;
    left: 60px; top: 952px;
    list-style: none;
  }
  .ticket-notes li { font-size: 27px; line-height: 35px; color: var(--accent-yellow); letter-spacing: 0.5px; }
  .venue-mark {
    position: absolute;
    left: 452px; top: 1040px;
    display: flex; align-items: center; gap: 12px;
  }
  .venue-mark__name { font-size: 56px; line-height: 1; color: var(--paper-white); letter-spacing: 1px; }
  .venue-info {
    position: absolute;
    left: 60px; right: 60px; top: 1100px;
    color: var(--muted-white);
  }
  .venue-info__heading { font-size: 19px; letter-spacing: 0.5px; }
  .venue-info__contacts {
    display: flex; justify-content: space-between;
    margin-top: 4px;
    font-size: 17px; letter-spacing: 0.5px;
  }
  .venue-info__divider { opacity: 0.8; }
  .venue-info__terms { font-size: 15px; letter-spacing: 0.5px; margin-top: 2px; }
</style>
</head>
<body>
  <main class="poster">
    <div class="stage-scene" role="img" aria-label="Crowd of dancers with raised hands silhouetted against colourful stage lights and sparkles"></div>
    <div class="crowd-band" aria-hidden="true"></div>

    <h1 class="event-title">
      <span class="event-title__main">COPPER</span>
      <span class="event-title__script">Moons</span>
    </h1>

    <section class="event-details">
      <p class="event-date">NEW YEARS EVE - 31.DEC.12</p>
      <p class="event-tagline">WHAT HAPPENS AT QUILL STAYS AT QUILL</p>
      <p class="event-time">8PM - 3AM</p>
    </section>

    <section class="package">
      <p class="package__price">$105 ALL INCLUSIVE</p>
      <ul class="package__list">
        <li><svg width="10" height="10" viewBox="0 0 10 10"><path d="M5 0 L6 4 L10 5 L6 6 L5 10 L4 6 L0 5 L4 4 Z" fill="var(--tag-cyan)"/></svg>INCLUDES A COCKTAIL ON ARRIVAL</li>
        <li><svg width="10" height="10" viewBox="0 0 10 10"><path d="M5 0 L6 4 L10 5 L6 6 L5 10 L4 6 L0 5 L4 4 Z" fill="var(--tag-cyan)"/></svg>4 HOUR DRINK PACKAGE - BASIC SPIRITS, PREMIUM BEER, WINE &amp; SPARKLING TIL 12AM</li>
        <li><svg width="10" height="10" viewBox="0 0 10 10"><path d="M5 0 L6 4 L10 5 L6 6 L5 10 L4 6 L0 5 L4 4 Z" fill="var(--tag-cyan)"/></svg>GRAZING STYLE CANAPÉS AND FINGER FOOD</li>
      </ul>
    </section>

    <ul class="ticket-notes">
      <li>EARLY BIRD AND GROUP DISCOUNTS (10+) AVAILABLE</li>
      <li>PURCHASE YOUR TICKETS AT THE BAR OR THROUGH THE WEBSITE</li>
      <li>DRESS - FOR FUN AND DANCING</li>
    </ul>

    <div class="venue-mark">
      <span class="venue-mark__name">QUILL APARTMENT</span>
    </div>

    <footer class="venue-info">
      <p class="venue-info__heading">VENUE INFORMATION</p>
      <p class="venue-info__contacts">
        <span>47 BRAMBLETON LANE ST KILDA</span>
        <span class="venue-info__divider">|</span>
        <span>6143 2057</span>
        <span class="venue-info__divider">|</span>
        <span>INFO@QUILLHOUSE.COM.AU</span>
        <span class="venue-info__divider">|</span>
        <span>WWW.QUILLHOUSE.COM.AU</span>
      </p>
      <p class="venue-info__terms">MANAGEMENT RESERVES THE RIGHT TO REFUSE ENTRY</p>
    </footer>
  </main>
</body>
</html>
```